larvosk.net

We are a IT Service for the valley. I want a clean website, with new Design, like animated pictures. We focus on IT. Give me your best design. What I'm looking for is eye catching. Works with Smart Phones, and iPad, Tab. Need a section for Submit a support tickets and Remote support. I'm looking for new ideals. I'm open mind, let me see what you guys can do.

Target Market(s)

My clients to see what service and products we have.

Industry/Entity Type

It Service

Requirements
Must have
• Able to submit a trouble tickets and works with Smart Phones, iPad, Tab.

```html
<!DOCTYPE html>
<html lang="en">
<head>
<meta charset="utf-8">
<title>Larvosk Technology</title>
<link rel="stylesheet" href="https://fonts.googleapis.com/css2?family=Oswald:wght@400;500;700&family=PT+Sans+Narrow:wght@400;700&display=swap">
<style>
:root{
  --red:#d8262e;
  --red-light:#e6464c;
  --navy:#2b3a5c;
  --ink:#333;
  --muted:#666;
  --blue-top:#5fb2d3;
  --blue-bottom:#2b7fad;
  --panel:#f3f3f3;
  --footer:#222;
  --white:#fff;
}
*{margin:0;padding:0;box-sizing:border-box}
html,body{width:1200px;height:943px;overflow:hidden;background:var(--white)}
body{position:relative;font-family:"PT Sans Narrow",sans-serif;color:var(--ink)}
.abs{position:absolute}

.site-header{left:0;top:7px;width:1200px;height:87px;border-top:1px solid #ddd;border-bottom:1px solid #ddd;
  background:repeating-linear-gradient(135deg,#f4f4f4 0 3px,#ececec 3px 5px)}
.brand{left:171px;top:16px;color:var(--navy);font-family:"Oswald",sans-serif;font-weight:500;white-space:nowrap}
.brand-name{font-size:40px;line-height:40px;letter-spacing:5px}
.brand-sub{font-size:15px;line-height:20px;letter-spacing:11px;font-weight:400;color:#333}
.main-nav{top:46px;left:0;font-size:14px;letter-spacing:2px;color:#444}
.main-nav a{position:absolute;color:inherit;text-decoration:none;white-space:nowrap}
.main-nav a.active{color:var(--red)}
.remote-support{left:846px;top:28px;width:183px;height:47px;background:var(--white);border:1px solid #ddd;box-shadow:0 1px 2px rgba(0,0,0,.08)}
.remote-avatar{left:4px;top:3px;width:40px;height:39px;background:linear-gradient(#e8c7a0,#b88a5c)}
.remote-title{left:56px;top:6px;font-size:14px;letter-spacing:2px;font-weight:700;color:#444;white-space:nowrap}
.remote-link{left:56px;top:25px;font-size:11px;letter-spacing:1px;color:var(--red);white-space:nowrap}

.hero{left:0;top:103px;width:1200px;height:307px;background:linear-gradient(var(--blue-top),var(--blue-bottom));border-top:3px solid #3d8fb9}
.hero-title{left:171px;top:19px;font-family:"Oswald",sans-serif;font-weight:700;font-size:48px;line-height:60px;letter-spacing:2px;color:#f2f2f2;text-shadow:0 2px 2px rgba(0,0,0,.3);white-space:nowrap}
.hero-text{left:171px;top:152px;width:460px;font-size:13px;line-height:22px;letter-spacing:1.1px;color:var(--white);text-shadow:0 1px 1px rgba(0,0,0,.4);white-space:nowrap}
.hero-btn{left:171px;top:220px;width:221px;height:46px;background:linear-gradient(var(--red-light),var(--red));border:2px solid #f06a6e;
  font-family:"Oswald",sans-serif;font-weight:700;font-size:18px;letter-spacing:3px;color:var(--white);text-align:center;line-height:42px}
.hero-device{left:694px;top:8px;width:305px;height:330px;background:linear-gradient(160deg,#cfd3d6,#8c949a 60%,#e6e6e6);border-radius:6px}

.intro-title{left:171px;top:428px;font-size:16px;font-weight:400;letter-spacing:1.5px;color:#333;white-space:nowrap}
.intro-text{left:171px;top:462px;font-size:12px;line-height:21px;letter-spacing:1.1px;color:#333;white-space:nowrap}
.intro-text a{color:var(--red);text-decoration:none}

.features{left:0;top:521px;width:1200px;height:334px;background:var(--panel);border-top:1px solid #e2e2e2;border-bottom:1px solid #e2e2e2}
.feature{top:25px;width:194px}
.feature-photo{width:194px;height:130px;background:var(--white);border:1px solid #ddd;padding:6px;box-shadow:0 1px 3px rgba(0,0,0,.1)}
.feature-photo div{width:100%;height:100%;background:linear-gradient(135deg,#cfe3ee,#6a9dba 55%,#1d3f5a)}
.feature-head{display:flex;align-items:center;gap:10px;height:22px;margin-top:24px;font-size:14px;letter-spacing:.9px;color:var(--navy);white-space:nowrap}
.feature-head svg{flex:none}
.feature-text{margin-top:8px;font-size:12.5px;line-height:25.5px;letter-spacing:1px;color:var(--muted);white-space:nowrap}
.feature-more{margin-top:8px;font-size:12.5px;letter-spacing:1.2px;color:var(--red)}

.site-footer{left:0;top:885px;width:1200px;height:58px;background:linear-gradient(#333,var(--footer));border-top:2px solid #555;
  font-size:10px;letter-spacing:1.5px;font-weight:700;color:var(--white)}
.footer-nav a{position:absolute;top:21px;color:inherit;text-decoration:none}
.footer-nav a.active{color:var(--red-light)}
.copyright{right:171px;top:21px;position:absolute}
.copyright span{color:var(--red-light)}
</style>
</head>
<body>

<header class="site-header abs">
  <div class="brand abs">
    <div class="brand-name">LARVOSK</div>
    <div class="brand-sub">TECHNOLOGY</div>
  </div>
  <nav class="main-nav abs">
    <a class="active" style="left:447px">HOME</a>
    <a style="left:535px">ABOUT</a>
    <a style="left:626px">SERVICES</a>
    <a style="left:737px">CONTACT</a>
  </nav>
  <div class="remote-support abs">
    <div class="remote-avatar abs" role="img" aria-label="Support agent with headset"></div>
    <div class="remote-title abs">REMOTE SUPPORT</div>
    <div class="remote-link abs">click here for more &gt;</div>
  </div>
</header>

<section class="hero abs">
  <div class="hero-device abs" role="img" aria-label="Desktop computer with keyboard and mouse"></div>
  <h1 class="hero-title abs">LOREM IPSUM DOLOR<br>AMET CONSECTETUR</h1>
  <p class="hero-text abs">Nam est ante, condimentum eu rhoncus sed, egestas a turpis. Phasellus<br>laoreet aliquet odio vitae adipiscing nullam hendrerit dignissim augue .</p>
  <div class="hero-btn abs">MORE INFO</div>
</section>

<h2 class="intro-title abs">LOREM IPSUM DOLOR SIT AMET, CONSECTETUR ADIPISCING</h2>
<p class="intro-text abs">Phasellus diam ligula, lobortis porta pretium ut, fermentum vel sapien. <a>Proin dictum</a>, tortor et dignissim hendrerit, nibh massa tincidunt ligula, id tristique<br>diam <a>justo a turpis</a>. Praesent tempus rhoncus odio, nec ornare ipsum euismod vel. Duis nisl massa, lacinia eelle &nbsp;<a>read more</a></p>

<section class="features abs">
  <article class="feature abs" style="left:173px">
    <div class="feature-photo"><div role="img" aria-label="Hands typing on a keyboard"></div></div>
    <div class="feature-head">
      <svg width="22" height="20" viewBox="0 0 22 20"><path d="M2 7h12v11H2z" fill="none" stroke="#2b3a5c" stroke-width="2"/><path d="M2 12h4l1 2h2l1-2h4" fill="none" stroke="#2b3a5c" stroke-width="2"/><circle cx="17" cy="4" r="3.5" fill="#2b3a5c"/></svg>
      LOREM IPSUM DOLOREN ON</div>
    <p class="feature-text">Praesent tempus rhoncus odio nect<br>ornare ipsum euismod vel. Duisalle<br>nislionermassa, lacinia eellen oner</p>
    <div class="feature-more">read more &gt;</div>
  </article>
  <article class="feature abs" style="left:395px">
    <div class="feature-photo"><div role="img" aria-label="Hands typing on a keyboard"></div></div>
    <div class="feature-head">
      <svg width="22" height="22" viewBox="0 0 22 22"><circle cx="11" cy="11" r="9" fill="none" stroke="#2b3a5c" stroke-width="2"/><path d="M16 6l3 4h-6z" fill="#2b3a5c"/><rect x="8" y="9" width="6" height="6" fill="#2b3a5c"/></svg>
      LOREM IPSUM DOLOREN ON</div>
    <p class="feature-text">Praesent tempus rhoncus odio nect<br>ornare ipsum euismod vel. Duisalle<br>nislionermassa, lacinia eellen oner</p>
    <div class="feature-more">read more &gt;</div>
  </article>
  <article class="feature abs" style="left:615px">
    <div class="feature-photo"><div role="img" aria-label="Hands typing on a keyboard"></div></div>
    <div class="feature-head">
      <svg width="22" height="16" viewBox="0 0 22 16"><rect x="1" y="1" width="20" height="14" fill="none" stroke="#2b3a5c" stroke-width="2"/><path d="M4 5h2M8 5h2M12 5h2M16 5h2M4 8h2M8 8h2M12 8h2M16 8h2M6 11h10" stroke="#2b3a5c" stroke-width="1.5"/></svg>
      LOREM IPSUM DOLOREN ON</div>
    <p class="feature-text">Praesent tempus rhoncus odio nect<br>ornare ipsum euismod vel. Duisalle<br>nislionermassa, lacinia eellen oner</p>
    <div class="feature-more">read more &gt;</div>
  </article>
  <article class="feature abs" style="left:836px">
    <div class="feature-photo"><div role="img" aria-label="Hands typing on a keyboard"></div></div>
    <div class="feature-head">
      <svg width="22" height="20" viewBox="0 0 22 20"><path d="M1 1h20v13H8l-5 5v-5H1z" fill="#2b3a5c"/><path d="M5 5h12M5 9h9" stroke="#fff" stroke-width="1.5"/></svg>
      LOREM IPSUM DOLOREN ON</div>
    <p class="feature-text">Praesent tempus rhoncus odio nect<br>ornare ipsum euismod vel. Duisalle<br>nislionermassa, lacinia eellen oner</p>
    <div class="feature-more">read more &gt;</div>
  </article>
</section>

<footer class="site-footer abs">
  <nav class="footer-nav">
    <a class="active" style="left:171px">home</a>
    <a style="left:229px">about</a>
    <a style="left:289px">services</a>
    <a style="left:359px">contact</a>
  </nav>
  <div class="copyright">Copyright © 2012 <span>larvosk.net</span> All rights reserved</div>
</footer>

</body>
</html>
```